Cover for Where the Lantern Drifts Beyond the Quiet Shore

Cover for a book that describes everything that happens to a person, from pre-birth life plans through growing in compassion and wisdom to death and living in the afterlife. The information is revealed in messages from people living in the life after this life. The title is Patterns Behind the Seasons of Your Journey and Beyond: Told by Voices Dwelling Past the Veil. Author is T. Milton Baxby. Book size is 6 by 9.

Target Market(s)

General

Font styles to use
Serif

```html
<!DOCTYPE html>
<html lang="en">
<head>
<meta charset="utf-8">
<title>Patterns Behind the Seasons of Your Journey and Beyond — T. Milton Baxby</title>
<link rel="stylesheet" href="https://fonts.googleapis.com/css2?family=Oswald:wght@600&family=Sorts+Mill+Goudy&display=swap">
<style>
  :root {
    --page: #ffffff;
    --ink-black: #000000;
    --title-white: #f6f3ee;
    --accent-orange: #f26a2e;
    --sky-top: #3a2230;
    --sky-mid: #4a3f63;
    --sky-rose: #b5506a;
    --sky-orange: #f07a3a;
    --sky-gold: #f8b24a;
  }
  * { margin: 0; padding: 0; box-sizing: border-box; }
  html, body {
    width: 1200px; height: 647px; overflow: hidden;
    background: var(--page);
  }
  .stage {
    position: relative; width: 1200px; height: 647px;
    display: flex; justify-content: center; align-items: center;
  }
  .book-cover {
    position: relative; width: 431px; height: 647px;
    background: var(--ink-black);
    overflow: hidden;
  }
  .cover-scene {
    position: absolute; left: 0; top: 0; width: 431px; height: 504px;
    display: block;
  }
  .author-name {
    position: absolute; top: 22px; right: 40px;
    font-family: "Oswald", "Arial Narrow", sans-serif;
    font-weight: 600; font-variant: small-caps;
    font-size: 26px; letter-spacing: 0.2px;
    color: var(--title-white); line-height: 1;
  }
  .title-block {
    position: absolute; left: 20px; right: 40px; top: 518px;
    text-align: right;
  }
  .book-title {
    font-family: "Sorts Mill Goudy", Georgia, serif;
    font-weight: 400; font-variant: small-caps;
    font-size: 23px; line-height: 32px;
    color: var(--title-white);
  }
  .book-title .title-line { display: block; white-space: nowrap; }
  .book-title .accent { color: var(--accent-orange); }
  .book-subtitle {
    margin-top: 16px;
    font-family: "Oswald", "Arial Narrow", sans-serif;
    font-weight: 600; font-variant: small-caps;
    font-size: 15px; letter-spacing: 0.1px;
    white-space: nowrap;
    color: var(--accent-orange); line-height: 1;
  }
</style>
</head>
<body>
  <main class="stage">
    <article class="book-cover">
      <svg class="cover-scene" viewBox="0 0 431 504" role="img"
           aria-label="Sunset sky with a large tree silhouette and figures of people at different stages of life walking across a hilltop">
        <defs>
          <linearGradient id="sunsetSky" x1="0" y1="0" x2="0" y2="1">
            <stop offset="0" stop-color="#3a2230"/>
            <stop offset="0.35" stop-color="#4a3f63"/>
            <stop offset="0.6" stop-color="#b5506a"/>
            <stop offset="0.8" stop-color="#f07a3a"/>
            <stop offset="0.95" stop-color="#f8b24a"/>
            <stop offset="1" stop-color="#000000"/>
          </linearGradient>
        </defs>
        <rect width="431" height="504" fill="url(#sunsetSky)"/>
      </svg>
      <p class="author-name">T. Milton Baxby</p>
      <div class="title-block">
        <h1 class="book-title">
          <span class="title-line">Patterns Behind the <span class="accent">Seasons</span></span>
          <span class="title-line">of Your <span class="accent">Journey</span> and <span class="accent">Beyond:</span></span>
        </h1>
        <p class="book-subtitle">Told by Voices Dwelling Past the Veil</p>
      </div>
    </article>
  </main>
</body>
</html>
```